Quiet River Psalter Reflections for Every Season of Long Waiting

This is not an Eastern meditation method. No images or themes from guru style or Eastern meditations from Hinduism or Buddhism will work. This is a Biblical Christian-based method. Some sort of Divine Light from Heaven may be the look. Some "ancient scroll" for the title to be written in may work.

```html
<!DOCTYPE html>
<html lang="en">
<head>
<meta charset="utf-8">
<title>Quiet River Psalter Reflections – Cover Spread</title>
<link rel="stylesheet" href="https://fonts.googleapis.com/css2?family=Cinzel:wght@400;500&family=Cormorant+Garamond:ital,wght@1,500&display=swap">
<style>
  :root {
    --ink: #2c1f14;
    --gold-deep: #5a3812;
    --gold-mid: #b07a2c;
    --gold-light: #e9c07a;
    --glow: #fff8e6;
    --white: #ffffff;
    --spine-ink: #fff3da;
  }
  html, body {
    margin: 0;
    padding: 0;
    overflow: hidden;
    background: #ffffff;
  }
  .cover-spread {
    position: relative;
    width: 1200px;
    height: 830px;
    overflow: hidden;
  }
  .sky-artwork {
    position: absolute;
    inset: 0;
    width: 1200px;
    height: 830px;
  }
  .rule {
    position: absolute;
    height: 2px;
  }
  .rule--back { left: 118px; top: 101px; width: 327px; background: var(--white); }
  .rule--front-top { left: 768px; top: 185px; width: 325px; background: var(--gold-deep); }
  .rule--front-bottom { left: 768px; top: 561px; width: 325px; background: var(--gold-deep); }

  .spine-text {
    position: absolute;
    left: 582px;
    top: 46px;
    width: 34px;
    writing-mode: vertical-rl;
    font-family: "Cinzel", serif;
    font-size: 21px;
    letter-spacing: 0.5px;
    white-space: nowrap;
    line-height: 34px;
  }
  .spine-text__title { color: var(--spine-ink); }
  .spine-text__author {
    color: var(--gold-deep);
    font-size: 14px;
    letter-spacing: 3px;
    margin-top: 46px;
  }

  .front-title {
    position: absolute;
    left: 652px;
    width: 548px;
    text-align: center;
    font-family: "Cinzel", serif;
    font-weight: 400;
    color: var(--ink);
    line-height: 1;
    white-space: nowrap;
  }
  .front-title--line1 { top: 208px; font-size: 58px; }
  .front-title--line2 { top: 290px; font-size: 96px; }
  .front-title--line3 { top: 420px; font-size: 56px; }
  .front-title--line4 { top: 486px; font-size: 52px; }

  .front-subtitle {
    position: absolute;
    left: 652px;
    top: 604px;
    width: 548px;
    text-align: center;
    font-family: "Cormorant Garamond", serif;
    font-style: italic;
    font-weight: 500;
    font-size: 33px;
    line-height: 40px;
    color: var(--ink);
  }
  .front-author {
    position: absolute;
    left: 652px;
    top: 734px;
    width: 548px;
    text-align: center;
    font-family: "Cinzel", serif;
    font-size: 40px;
    color: var(--white);
    line-height: 1;
  }
</style>
</head>
<body>
<main class="cover-spread">
  <svg class="sky-artwork" viewBox="0 0 1200 830" role="img" aria-label="Golden clouded heavenly sky with rays of light breaking through, wrapping across back cover, spine and front cover">
    <defs>
      <linearGradient id="skyBase" x1="0" y1="0" x2="0" y2="1">
        <stop offset="0" stop-color="#9a6a2a"/>
        <stop offset="0.5" stop-color="#b4823a"/>
        <stop offset="1" stop-color="#6e4618"/>
      </linearGradient>
      <radialGradient id="frontGlow" cx="0.78" cy="0.45" r="0.38">
        <stop offset="0" stop-color="#ffffff"/>
        <stop offset="0.25" stop-color="#fff4dc"/>
        <stop offset="0.6" stop-color="#e3b76e" stop-opacity="0.6"/>
        <stop offset="1" stop-color="#b4823a" stop-opacity="0"/>
      </radialGradient>
      <radialGradient id="backGlow" cx="0.46" cy="0.02" r="0.45">
        <stop offset="0" stop-color="#fff6e0"/>
        <stop offset="0.4" stop-color="#e8c07e" stop-opacity="0.7"/>
        <stop offset="1" stop-color="#b4823a" stop-opacity="0"/>
      </radialGradient>
      <radialGradient id="shade" cx="0.2" cy="0.7" r="0.5">
        <stop offset="0" stop-color="#5a3812" stop-opacity="0.45"/>
        <stop offset="1" stop-color="#5a3812" stop-opacity="0"/>
      </radialGradient>
    </defs>
    <rect width="1200" height="830" fill="url(#skyBase)"/>
    <rect width="1200" height="830" fill="url(#shade)"/>
    <rect width="1200" height="830" fill="url(#backGlow)"/>
    <rect width="1200" height="830" fill="url(#frontGlow)"/>
  </svg>

  <div class="rule rule--back"></div>

  <div class="spine-text">
    <span class="spine-text__title">QUIET RIVER PSALTER REFLECTIONS</span>
    <span class="spine-text__author">THOMAS AVERY</span>
  </div>

  <div class="rule rule--front-top"></div>
  <h1 class="front-title front-title--line1">QUIET RIVER</h1>
  <div class="front-title front-title--line2">PSALTER</div>
  <div class="front-title front-title--line3">REFLECTIONS</div>
  <div class="rule rule--front-bottom"></div>

  <p class="front-subtitle">for Every Season<br>of Long Waiting</p>
  <p class="front-author">THOMAS AVERY</p>
</main>
</body>
</html>
```